Web page design for podiatry office*

Need a web page for our podiatry office. It should feature most of our services, hours, directions and location. Should include a short bio of the doctor and a contact page.

Coding

Coded - Design and coding required

Number of Pages Required

1 page

Colors

Designer to choose colors to be used in the design.

```html
<!DOCTYPE html>
<html lang="en">
<head>
<meta charset="utf-8">
<title>Stride Foot Clinic</title>
<link rel="stylesheet" href="https://fonts.googleapis.com/css2?family=Montserrat:wght@500;600;700;800&family=Lato:wght@400;700&display=swap">
<style>
:root{
  --blue:#1a8fd6;
  --blue-deep:#0a7fc4;
  --green:#4cb82a;
  --teal-a:#3aaedb;
  --teal-b:#36c4a2;
  --ink:#2b2b2b;
  --muted:#555;
  --footer:#0d2230;
  --footer-base:#0a1b27;
  --grey-panel:#54585c;
  --band:#e4e4e4;
  --white:#fff;
}
*{margin:0;padding:0;box-sizing:border-box}
html,body{width:1200px;height:3558px;overflow:hidden}
body{font-family:"Lato",Arial,sans-serif;color:var(--ink);background:var(--white);position:relative}
.abs{position:absolute}
section,header,footer{position:absolute;left:0;width:1200px}
h1,h2,h3,h4{font-family:"Montserrat",Arial,sans-serif}

/* header */
.topbar{top:0;height:80px}
.brand{left:159px;top:22px;display:flex;align-items:center;gap:8px;font-family:"Montserrat",sans-serif;font-weight:700;font-size:24px;color:var(--blue)}
.brand-dot{width:22px;height:22px;border-radius:50%;background:var(--green)}
.info{display:flex;align-items:center;gap:12px;top:24px}
.info-icon{width:38px;height:38px;border-radius:50%;background:var(--blue);display:flex;align-items:center;justify-content:center}
.info-text{font-size:11px;color:#444;line-height:16px}
.info-text b{font-family:"Montserrat",sans-serif;font-size:10px;font-weight:700;color:#333}
.nav{top:80px;height:66px;border-top:1px solid #eee;border-bottom:2px solid var(--green)}
.nav a{position:absolute;top:21px;font-size:15px;color:#555;text-decoration:none;font-family:"Montserrat",sans-serif;font-weight:500}
.nav a.active{color:var(--blue);font-weight:700}
.nav a.active::before{content:"";position:absolute;left:18px;top:-21px;width:2px;height:12px;background:#ccc}
.social i{position:absolute;width:14px;height:14px;border-radius:50%;background:#777}

/* hero */
.hero{top:146px;height:482px;background:linear-gradient(100deg,#d9d4cf 0%,#efe6df 35%,#f3ece6 55%,#c9d3d9 80%,#aebcc5 100%)}
.hero h1{position:absolute;left:222px;top:130px;font-size:36px;line-height:44px;font-weight:600;color:#222;letter-spacing:-0.5px}
.hero p{position:absolute;left:222px;top:240px;font-size:12.5px;line-height:22px;color:#333;width:340px}
.btn{display:flex;align-items:center;justify-content:center;border-radius:22px;background:var(--blue);color:#fff;font-family:"Montserrat",sans-serif;font-weight:700;text-transform:uppercase}
.hero .btn{position:absolute;left:222px;top:310px;width:125px;height:34px;font-size:13px}
.arrow-btn{position:absolute;top:351px;width:50px;height:50px;border-radius:50%;background:rgba(255,255,255,.55);display:flex;align-items:center;justify-content:center}
.dot{position:absolute;left:171px;width:7px;height:7px;border-radius:50%;background:var(--blue)}

/* features */
.features{top:628px;height:270px;display:flex}
.feature{flex:1;text-align:center;color:#fff;padding-top:55px}
.feature:nth-child(1){background:#38a9d6}
.feature:nth-child(2){background:#37b0cf}
.feature:nth-child(3){background:#37b8c0}
.feature:nth-child(4){background:#36c2a8}
.feature-icon{width:56px;height:56px;margin:0 auto;border-radius:50%;background:#fff;display:flex;align-items:center;justify-content:center}
.feature h3{font-size:22px;font-weight:700;margin-top:14px}
.feature p{font-size:12.5px;line-height:22px;margin:10px auto 0;width:210px}

/* bio */
.bio{top:898px;height:625px}
.section-title{position:absolute;left:0;width:1200px;text-align:center;font-weight:800;color:#222}
.bio .section-title{top:76px;font-size:33px}
.bio .lead{position:absolute;left:0;width:1200px;top:132px;text-align:center;font-size:12px;line-height:22px;color:#444}
.doctor-photo{left:463px;top:193px;width:255px;height:430px;border-radius:120px 120px 0 0;background:linear-gradient(180deg,#5a3a2c 0%,#8a5c46 30%,#eef1f4 45%,#ffffff 100%)}
.sub-head{display:flex;align-items:center;gap:14px;font-family:"Montserrat",sans-serif;font-weight:700;font-size:22px;color:#555}
.sub-icon{width:56px;height:56px;border-radius:50%;background:var(--blue);display:flex;align-items:center;justify-content:center}
.bio-text{left:160px;width:270px;font-size:11.5px;line-height:22.5px;color:#444}
.qual{left:783px;top:324px;font-size:12px;line-height:34.5px}
.qual div{display:flex}
.qual b{width:109px;font-family:"Montserrat",sans-serif;font-size:11px;color:#222}
.qual span{color:#444}

/* appointment */
.appointment{top:1519px;height:334px}
.appointment .bg{left:0;top:24px;width:1200px;height:310px;background:linear-gradient(90deg,#0a7ec3 0%,#0b84c8 60%,#2d7fb0 80%,#3a7ca6 100%)}
.appointment .photo{left:860px;top:24px;width:340px;height:310px;background:linear-gradient(100deg,rgba(10,126,195,0) 0%,rgba(80,130,160,.55) 50%,rgba(40,105,150,.5) 100%)}
.appointment h2{top:80px;font-size:45px;color:#fff;left:6px}
.field{position:absolute;top:175px;width:232px;height:32px;background:#fff;font-size:10px;color:#aaa;padding:11px 14px;display:flex;justify-content:space-between}
.submit-req{left:489px;top:236px;width:232px;height:36px;border:1px solid #fff;color:#fff;font-family:"Montserrat",sans-serif;font-weight:700;font-size:10.5px;display:flex;align-items:center;justify-content:center}

/* location */
.location{top:1853px;height:451px}
.location h2{position:absolute;font-size:35px;font-weight:700;color:#333;line-height:40px}
.map{left:162px;top:129px;width:535px;height:236px;background:linear-gradient(135deg,#e7efe4 0%,#f2eee6 40%,#f8efc9 60%,#e2e8ee 100%)}
.address{left:744px;top:158px;font-size:19px;line-height:34.5px;color:#444}
.location .btn{position:absolute;left:744px;top:329px;width:136px;height:28px;font-size:12px;box-shadow:0 3px 8px rgba(0,0,0,.2)}

/* contact */
.contact{top:2304px;height:555px}
.contact .left{left:0;top:0;width:600px;height:555px;background:var(--blue-deep)}
.contact .right{left:600px;top:0;width:600px;height:555px;background:var(--grey-panel)}
.contact h2{left:163px;top:74px;font-size:37px;font-weight:800;color:#0c1a2a}
.contact .intro{left:168px;top:131px;width:400px;font-size:13px;line-height:22px;color:#0d2a45}
.contact .org{left:163px;top:231px;font-family:"Lato",sans-serif;font-size:25px;color:#fff}
.c-line{left:163px;display:flex;align-items:center;gap:20px;font-size:13px;color:#0c1a2a}
.c-line svg{flex:none}
.form-label{left:679px;font-size:10px;color:#fff}
.form-line{left:677px;width:294px;height:1px;background:#c9c9c9}
.contact .btn{position:absolute;left:674px;top:444px;width:142px;height:37px;font-size:15px;box-shadow:0 3px 8px rgba(0,0,0,.3)}

/* offer */
.offer{top:2859px;height:131px;background:var(--band)}
.offer p{left:191px;top:56px;font-family:"Montserrat",sans-serif;font-weight:700;font-size:22px;color:#333}
.offer .btn{position:absolute;left:882px;top:51px;width:143px;height:38px;font-size:15px}

/* footer */
.site-footer{top:2990px;height:568px;background:var(--footer)}
.site-footer h4{position:absolute;top:78px;font-size:16px;font-weight:700;color:#fff;letter-spacing:.3px}
.f-text{font-size:12px;line-height:18px;color:#c5ccd2}
.links{font-size:11.5px;color:#c5ccd2;line-height:29px}
.links div{position:relative;padding-left:21px}
.links div::before{content:"";position:absolute;left:0;top:11px;border-left:5px solid var(--blue);border-top:4px solid transparent;border-bottom:4px solid transparent}
.f-label{left:872px;font-size:12px;color:#c5ccd2}
.f-line{left:871px;width:176px;height:1px;background:#4a5a66}
.f-submit{left:874px;top:320px;width:93px;height:25px;font-size:10px;border-radius:14px}
.f-social i{position:absolute;top:374px;width:14px;height:14px;border-radius:50%;background:#fff}
.base{left:0;top:469px;width:1200px;height:99px;background:var(--footer-base);text-align:center;font-size:9.5px;color:#aeb8c0;padding-top:42px}
</style>
</head>
<body>

<header class="topbar">
  <div class="abs brand"><span class="brand-dot"></span>Stride Foot Clinic</div>
  <div class="abs info" style="left:467px">
    <div class="info-icon"><svg width="18" height="18" viewBox="0 0 18 18"><circle cx="9" cy="9" r="7" fill="none" stroke="#fff" stroke-width="2"/><path d="M9 5v4l3 2" stroke="#fff" stroke-width="2" fill="none"/></svg></div>
    <div class="info-text"><b>WORK TIME: 09:00 - 17:00</b><br>Saturday and Sunday - CLOSED</div>
  </div>
  <div class="abs info" style="left:726px">
    <div class="info-icon"><svg width="18" height="14" viewBox="0 0 18 14"><rect x="1" y="1" width="16" height="12" rx="1" fill="#fff"/><path d="M1 2l8 6 8-6" stroke="#1a8fd6" stroke-width="1.5" fill="none"/></svg></div>
    <div class="info-text"><b>MAIL US</b><br>hello@stridefootclinic.example</div>
  </div>
  <div class="abs info" style="left:925px">
    <div class="info-icon"><svg width="12" height="18" viewBox="0 0 12 18"><rect x="1" y="1" width="10" height="16" rx="2" fill="none" stroke="#fff" stroke-width="2"/><circle cx="6" cy="14" r="1" fill="#fff"/></svg></div>
    <div class="info-text"><b>CALL US</b><br>+1 555 0142 7700</div>
  </div>
</header>

<nav class="abs nav" style="left:0;width:1200px">
  <a class="active" style="left:159px">Home</a>
  <a style="left:231px">About</a>
  <a style="left:301px">Services</a>
  <a style="left:387px">Gallery</a>
  <a style="left:467px">Blog</a>
  <a style="left:528px">Contact us</a>
  <div class="social"><i style="left:896px;top:27px"></i><i style="left:932px;top:27px"></i><i style="left:973px;top:27px"></i><i style="left:1009px;top:27px"></i><i style="left:1044px;top:27px"></i></div>
</nav>

<section class="hero" role="img" aria-label="Photo of a podiatrist in gloves examining a patient's foot">
  <h1>We have Best Podiatry<br>plan options for you</h1>
  <p>Sed ut perspiciatis unde omnis iste natus error sit volup­tatem accusantium doloremque laudantium.</p>
  <div class="btn">Read More</div>
  <div class="arrow-btn" style="left:152px"><svg width="26" height="12" viewBox="0 0 26 12"><path d="M25 6H2M7 1L2 6l5 5" stroke="#666" stroke-width="1.5" fill="none"/></svg></div>
  <div class="arrow-btn" style="left:1013px"><svg width="26" height="12" viewBox="0 0 26 12"><path d="M1 6h23M19 1l5 5-5 5" stroke="#666" stroke-width="1.5" fill="none"/></svg></div>
  <span class="dot" style="top:380px"></span>
  <span class="dot" style="top:400px;width:13px;height:13px;left:168px;background:var(--green)"></span>
  <span class="dot" style="top:420px"></span>
  <span class="dot" style="top:438px"></span>
</section>

<svg class="abs" style="left:0;top:598px" width="1200" height="32" viewBox="0 0 1200 32"><path d="M0 14Q600 40 1200 8V32H0Z" fill="var(--green)"/></svg>

<section class="features">
  <div class="feature">
    <div class="feature-icon"><svg width="28" height="28" viewBox="0 0 28 28" fill="none" stroke="#1a8fd6" stroke-width="2"><path d="M8 3v8a6 6 0 0012 0V3"/><path d="M14 17v4a4 4 0 008 0v-2"/><circle cx="22" cy="17" r="2"/></svg></div>
    <h3>Best Podiatry</h3>
    <p>Sed ut perspiciatis unde omnis iste natus error sit voluptatem accusan­tium doloremque laudantium.</p>
  </div>
  <div class="feature">
    <div class="feature-icon"><svg width="28" height="28" viewBox="0 0 28 28" fill="none" stroke="#1a8fd6" stroke-width="2"><path d="M5 6c0 9 8 17 17 17l2-4-5-3-2 2c-3-1-6-4-7-7l2-2-3-5z"/><circle cx="20" cy="8" r="5"/><path d="M20 5v6M17 8h6"/></svg></div>
    <h3>Emergency Help</h3>
    <p>Sed ut perspiciatis unde omnis iste natus error sit voluptatem accusan­tium doloremque laudantium.</p>
  </div>
  <div class="feature">
    <div class="feature-icon"><svg width="28" height="28" viewBox="0 0 28 28" fill="none" stroke="#1a8fd6" stroke-width="2"><rect x="9" y="3" width="10" height="5"/><circle cx="14" cy="12" r="4"/><path d="M6 26v-4a8 8 0 0116 0v4"/></svg></div>
    <h3>Medical Staff</h3>
    <p>Sed ut perspiciatis unde omnis iste natus error sit voluptatem accusan­tium doloremque laudantium.</p>
  </div>
  <div class="feature">
    <div class="feature-icon"><svg width="30" height="24" viewBox="0 0 30 24" fill="none" stroke="#1a8fd6" stroke-width="2"><path d="M2 18V6h17v12M19 10h5l4 5v3H2"/><circle cx="8" cy="19" r="2.5"/><circle cx="22" cy="19" r="2.5"/><path d="M10 9v6M7 12h6"/></svg></div>
    <h3>PodiatryDoctors</h3>
    <p>Sed ut perspiciatis unde omnis iste natus error sit voluptatem accusan­tium doloremque laudantium.</p>
  </div>
</section>

<div class="abs" style="left:565px;top:593px;width:70px;height:70px;border-radius:50%;background:#fff;border:4px solid var(--green);display:flex;align-items:center;justify-content:center"><svg width="16" height="22" viewBox="0 0 16 22"><path d="M8 1v19M2 14l6 6 6-6" stroke="#555" stroke-width="1.5" fill="none"/></svg></div>

<section class="bio">
  <h2 class="section-title">SHORT BIO OF THE DOCTOR</h2>
  <p class="lead">Lorem ipsum dolor sit amet, consectetur adipiscing elit, sed do eiusmod tempor incididunt ut labore et dolore magna aliqua.<br>Ut enim ad minim veniam, quis nostrud exercitation ullamco laboris nisi ut aliquip ex ea commodo consequat.</p>
  <div class="abs doctor-photo" role="img" aria-label="Portrait photo of the doctor in a white coat with a stethoscope"></div>

  <div class="abs sub-head" style="left:161px;top:263px">
    <div class="sub-icon"><svg width="30" height="30" viewBox="0 0 30 30" fill="none" stroke="#fff" stroke-width="2"><path d="M12 3h6v8l7-4 3 5-7 4 7 4-3 5-7-4v8h-6v-8l-7 4-3-5 7-4-7-4 3-5 7 4z"/></svg></div>SHORT BIO
  </div>
  <p class="abs bio-text" style="top:327px">Lorem ipsum dolor sit amet, consectetur adipiscing elit, sed do eiusmod tempor incididunt ut labore et dolore magna aliqua. Ut enim ad minim veniam, quis nostrud exercitation ullamco laboris nisi ut aliquip ex ea commodo consequat.</p>
  <p class="abs bio-text" style="top:462px">Lorem ipsum dolor sit amet, consectetur adipiscing elit, sed do eiusmod tempor incididunt ut labore et dolore magna aliqua. Ut enim ad minim veniam, quis nostrud exercitation ullamco laboris nisi ut aliquip ex ea commodo consequat.</p>

  <div class="abs sub-head" style="left:780px;top:257px">
    <div class="sub-icon"><svg width="32" height="32" viewBox="0 0 32 32" fill="none" stroke="#fff" stroke-width="1.8"><ellipse cx="16" cy="16" rx="13" ry="5"/><ellipse cx="16" cy="16" rx="13" ry="5" transform="rotate(60 16 16)"/><ellipse cx="16" cy="16" rx="13" ry="5" transform="rotate(120 16 16)"/><circle cx="16" cy="16" r="2" fill="#fff"/></svg></div>QUALIFICATION
  </div>
  <div class="abs qual">
    <div><b>NAME:</b><span>Maren Ellis</span></div>
    <div><b>AGE:</b><span>30 years</span></div>
    <div><b>DEGREE:</b><span>FRCS(LONDON)</span></div>
    <div><b>EXPERIENCE:</b><span>2 years</span></div>
    <div><b>COUNTRY:</b><span>USA</span></div>
    <div><b>WORK NOW:</b><span>Stride Foot Clinic</span></div>
  </div>
</section>

<section class="appointment">
  <svg class="abs" style="left:0;top:0" width="1200" height="26" viewBox="0 0 1200 26"><path d="M0 0Q600 40 1200 0V26H0Z" fill="var(--green)"/></svg>
  <div class="abs bg"></div>
  <div class="abs photo" role="img" aria-label="Photo of a surgeon in a cap, tinted blue"></div>
  <h2 class="section-title">MAKE AN APPOINTMENT</h2>
  <div class="field" style="left:221px">Select Doctor<svg width="8" height="5" viewBox="0 0 8 5"><path d="M0 0h8L4 5z" fill="#999"/></svg></div>
  <div class="field" style="left:486px">Choose Date<svg width="9" height="9" viewBox="0 0 9 9"><rect x=".5" y="1.5" width="8" height="7" fill="none" stroke="#aaa"/></svg></div>
  <div class="field" style="left:751px">Select Time<svg width="9" height="9" viewBox="0 0 9 9"><circle cx="4.5" cy="4.5" r="4" fill="none" stroke="#aaa"/></svg></div>
  <div class="abs submit-req">SUBMIT YOU REQUIREMENTS</div>
</section>

<div class="abs" style="left:565px;top:1502px;width:70px;height:70px;border-radius:50%;background:#fff;border:4px solid var(--green);display:flex;align-items:center;justify-content:center"><svg width="16" height="22" viewBox="0 0 16 22"><path d="M8 1v19M2 14l6 6 6-6" stroke="#555" stroke-width="1.5" fill="none"/></svg></div>

<section class="location">
  <h2 style="left:164px;top:56px">Our Location</h2>
  <div class="abs map" role="img" aria-label="Street map of the clinic's neighbourhood in Lakeside City"></div>
  <h2 style="left:742px;top:56px">Podiatry Office<br>Directions</h2>
  <div class="abs address">Demo Road 123 Street,<br>Lakeside 652,<br>Zip Code 123456<br>USA</div>
  <div class="btn">Get Direction</div>
</section>

<section class="contact">
  <div class="abs left"></div>
  <div class="abs right"></div>
  <h2 class="abs">CONTACT US</h2>
  <p class="abs intro">Lorem ipsum dolor sit amet, consectetur adipiscing elit, sed do eiusmod tempor incididunt ut labore et dolore magna aliqua.</p>
  <div class="abs org">StrideFootClinic</div>
  <div class="abs c-line" style="top:279px"><svg width="18" height="18" viewBox="0 0 18 18"><rect width="18" height="18" rx="3" fill="#fff"/><path d="M5 4c0 6 3 9 9 10l1-3-3-1-1 1c-2-1-3-2-4-4l1-1-1-3z" fill="#0a7fc4"/></svg>+1 (555) 310-4826</div>
  <div class="abs c-line" style="top:308px"><svg width="18" height="14" viewBox="0 0 18 14"><rect x="1" y="1" width="16" height="12" fill="none" stroke="#fff" stroke-width="1.5"/><path d="M1 1l8 6 8-6" stroke="#fff" stroke-width="1.5" fill="none"/></svg>care@stridefootclinic.example</div>
  <div class="abs c-line" style="top:334px"><svg width="18" height="22" viewBox="0 0 18 22"><path d="M3 2v15l4-4 3 7 3-1-3-7h6z" fill="#fff"/></svg>www.stridefootclinic.example</div>

  <div class="abs form-label" style="top:140px">Name</div><div class="abs form-line" style="top:162px"></div>
  <div class="abs form-label" style="top:200px">Email</div><div class="abs form-line" style="top:222px"></div>
  <div class="abs form-label" style="top:260px">Subject</div><div class="abs form-line" style="top:283px"></div>
  <div class="abs form-label" style="top:306px">Message</div><div class="abs form-line" style="top:410px"></div>
  <div class="btn">Send</div>
</section>

<section class="offer">
  <p class="abs">New Patient Special Offer Complimentary Consultation</p>
  <div class="btn">Read More</div>
</section>
<svg class="abs" style="left:0;top:2960px" width="1200" height="32" viewBox="0 0 1200 32"><path d="M0 6Q600 44 1200 6V32H0Z" fill="var(--blue)"/></svg>

<footer class="site-footer">
  <h4 style="left:153px">Get in Touch</h4>
  <h4 style="left:424px">Quick Links</h4>
  <h4 style="left:632px">Our Services</h4>
  <h4 style="left:871px">Enquiry Form</h4>

  <svg class="abs" style="left:153px;top:150px" width="30" height="22" viewBox="0 0 30 22"><rect x="1" y="1" width="28" height="20" fill="none" stroke="#9aa6ae" stroke-width="1.5"/><path d="M1 1l14 11L29 1" stroke="#9aa6ae" stroke-width="1.5" fill="none"/></svg>
  <div class="abs f-text" style="left:217px;top:151px">hello@stridefootclinic.example</div>
  <svg class="abs" style="left:157px;top:205px" width="20" height="32" viewBox="0 0 20 32"><rect x="1" y="1" width="18" height="30" rx="2" fill="none" stroke="#9aa6ae" stroke-width="1.5"/><path d="M1 6h18M1 25h18" stroke="#9aa6ae" stroke-width="1.5"/></svg>
  <div class="abs f-text" style="left:213px;top:212px">+1 555 0188 2040<br>+1 555 0188 2040</div>
  <svg class="abs" style="left:152px;top:280px" width="32" height="32" viewBox="0 0 32 32"><path d="M16 3a8 8 0 018 8c0 7-8 14-8 14s-8-7-8-14a8 8 0 018-8z" fill="none" stroke="#9aa6ae" stroke-width="1.5"/><circle cx="16" cy="11" r="3" fill="none" stroke="#9aa6ae" stroke-width="1.5"/><path d="M6 22l-4 8h28l-4-8" fill="none" stroke="#9aa6ae" stroke-width="1.5"/></svg>
  <div class="abs f-text" style="left:217px;top:288px">123, Main Road, New City,<br>Lakeside 123456</div>
  <div class="f-social"><i style="left:156px"></i><i style="left:195px"></i><i style="left:243px"></i><i style="left:283px"></i><i style="left:321px"></i></div>

  <div class="abs links" style="left:436px;top:138px">
    <div>About us</div><div>Blog</div><div>Contact us</div><div>Faq</div><div>Insurance</div><div>Contact us</div>
  </div>
  <div class="abs links" style="left:632px;top:138px">
    <div>Podiatry Service</div><div>Podiatry Service</div><div>Podiatry Service</div><div>Podiatry Service</div><div>Podiatry Service</div><div>Podiatry Service</div>
  </div>

  <div class="abs f-label" style="top:141px">Name</div><div class="abs f-line" style="top:168px"></div>
  <div class="abs f-label" style="top:184px">Phone</div><div class="abs f-line" style="top:211px"></div>
  <div class="abs f-label" style="top:228px">Message</div><div class="abs f-line" style="top:301px"></div>
  <div class="abs btn f-submit">Submit</div>

  <div class="abs base">Copyright © 2019. stridefootclinic.example &nbsp;|&nbsp; Terms &amp; Conditions &nbsp; | &nbsp; Privacy Policy</div>
</footer>

<div class="abs" style="left:566px;top:2951px;width:68px;height:68px;border-radius:50%;background:#fff;border:4px solid var(--blue);display:flex;align-items:center;justify-content:center"><svg width="16" height="22" viewBox="0 0 16 22"><path d="M8 21V2M2 8l6-6 6 6" stroke="#555" stroke-width="1.5" fill="none"/></svg></div>

</body>
</html>
```